I need a cd cover my CD. The cd is about my journey in my recovery from addiction. The name of the CD is Hall of Quiet Embers. I would like something artsy that reflects the song. The song is a metaphor so I am not looking for something where doors are the main emphasis for the cover. During my addiction I burned a lot of bridges, hurt a lot of people, hurt myself and my 3 1/2 year old son died in a house fire while I was sitting in a jail cell. So the hall of Quiet Embers song is a battle that I have in my head... sometimes on a daily basis about picking up and using again. So I play the tape of my life in my head of all of the crap that I've created and what I've done. When I do that, it stops me from relapsing, because I know what will happen if I do.

I don't want a photo. I also want my name on the cd to be Nate R. Don't add my last name just the initial. I've attached the link to the song and also another song called Rise Slow. Also that you can get a feel for it. Also disregard the image that's on ViewLoop.

https://www.viewloop-media.test/watch?v=Qm7rTz2KpL0&t=42s

https://www.viewloop-media.test/watch?v=Hn3wEs8YbFc

Target Market(s)

People in Recovery, Sobriety

Industry/Entity Type

Music Download

Font styles to use
Serif

Colors

Requirements
Must have
• A mysterious feel to it.
Nice to have
• The song is about my secret space which is actually inside my mind. It's a place I go to, kind of like a tape I play that in my head that if I relapse, This will happen and that will happen etc... I also want something that will look good on a T-Shirt and Hats etc...
Should not have
• Nothing Gothic and no Photographs.

```html
<!DOCTYPE html>
<html lang="en">
<head>
<meta charset="utf-8">
<title>Nate R. — Hall of Quiet Embers</title>
<link rel="stylesheet" href="https://fonts.googleapis.com/css2?family=Cinzel:wght@400;700&display=swap">
<style>
  :root {
    --stage: #1e1e1e;
    --panel-deep: #17130f;
    --panel-warm: #231b15;
    --sleeve: #f2f2f2;
    --ink: #4e3a2c;
    --headline: #ffffff;
    --art-light: #e4c7b4;
    --art-mid: #c9a892;
    --art-dark: #6e5a4a;
  }
  * { margin: 0; padding: 0; box-sizing: border-box; }
  html, body {
    width: 1200px;
    height: 857px;
    overflow: hidden;
    background: var(--stage);
  }
  .stage {
    position: relative;
    width: 1200px;
    height: 857px;
    background: var(--stage);
  }
  .backdrop {
    position: absolute;
    left: 634px;
    top: 0;
    width: 566px;
    height: 857px;
    background:
      linear-gradient(90deg, var(--stage) 0%, var(--panel-warm) 22%, var(--panel-deep) 60%, var(--panel-warm) 100%);
  }
  .album-cover {
    position: absolute;
    left: 105px;
    top: 135px;
    width: 569px;
    height: 568px;
    background: var(--sleeve);
  }
  .cover-art {
    position: absolute;
    left: 227px;
    top: 54px;
    width: 126px;
    height: 407px;
    background:
      linear-gradient(180deg, #d9d2cc 0%, var(--art-light) 14%, var(--art-mid) 48%, var(--art-light) 70%, #b79b84 84%, var(--art-dark) 100%);
    clip-path: polygon(1% 6%, 97% 5%, 100% 98%, 0% 100%);
  }
  .cover-credit {
    position: absolute;
    left: 0;
    right: 0;
    top: 497px;
    text-align: center;
    font-family: "Cinzel", serif;
    font-size: 14px;
    letter-spacing: 0.12em;
    color: var(--ink);
    text-transform: uppercase;
    white-space: nowrap;
  }
  .cover-credit .artist { font-weight: 700; }
  .cover-credit .title { font-weight: 400; }
  .headline {
    position: absolute;
    left: 726px;
    top: 622px;
    color: var(--headline);
    font-family: "Cinzel", serif;
    text-transform: uppercase;
    white-space: nowrap;
  }
  .headline-artist {
    display: block;
    font-size: 52px;
    font-weight: 700;
    line-height: 1;
    letter-spacing: 0.16em;
  }
  .headline-title {
    display: block;
    margin-top: 8px;
    font-size: 21px;
    font-weight: 700;
    line-height: 1;
    letter-spacing: 0.1em;
  }
</style>
</head>
<body>
  <main class="stage">
    <div class="backdrop" role="img" aria-label="Dark, softly blurred view of the same doorway scene enlarged behind the album"></div>
    <section class="album-cover">
      <div class="cover-art" role="img" aria-label="Narrow vertical scene of a worn doorway at the top of a short flight of weathered steps, lit by a single ceiling lamp"></div>
      <p class="cover-credit"><span class="artist">Nate R.</span> <span class="title">Hall of Quiet Embers</span></p>
    </section>
    <h1 class="headline">
      <span class="headline-artist">Nate R.</span>
      <span class="headline-title">Hall of Quiet Embers</span>
    </h1>
  </main>
</body>
</html>
```